Tidewell Cryotherapy brochure

I need brochure design for my Cryotherapy business.
Target market: Athletes from high School to pro, Fitness, adults needing relief from arthritic and surgical pain. Color pallet should have be in keeping with the logo blues, white and silver (attached). There should be a sections to address what full body cryo is .. and its benefits, FAQ's. a section that i can list services, prices, hours...ect.. There should also be high quality pics in keeping with the theme of rejuvenation and replenishment. Tri Fold double sided.

Target Market(s)

Target market: Athletes from high School to pro, Fitness, adults needing relief from arthritic and surgical pain.

Industry/Entity Type

Business

Colors
33a6d7
cee9f5
0255a3
cfdeed
ffffff
ecf7fb
d7d7d7
9d9d9d

Requirements
Must have
• There should be a sections to address what full body cryo is .. and its benefits, FAQ's. a section that i can list services, prices, hours...ect.. There should also be high quality pics in keeping with the theme of rejuvenation and replenishment. Tri Fold double sided.
Nice to have
• Graphics of the circulatrory system and cryo's effect on it.

```html
<!DOCTYPE html>
<html lang="en">
<head>
<meta charset="utf-8">
<title>Tidewell Cryotherapy – Tri-fold Brochure</title>
<link href="https://fonts.googleapis.com/css2?family=Montserrat:wght@400;500;600&family=Oswald:wght@500;700&display=swap" rel="stylesheet">
<style>
:root{
  --stage:#d1d2d4;
  --navy:#1c3a60;
  --navy-deep:#0b2447;
  --ink:#04070d;
  --sky:#33a6d7;
  --bright:#1f9fe6;
  --white:#ffffff;
  --ice:#cee9f5;
}
*{margin:0;padding:0;box-sizing:border-box}
html,body{width:1200px;height:1000px;overflow:hidden;background:var(--stage)}
.canvas{position:relative;width:1200px;height:1000px}
.brochure{position:absolute;left:104px;top:114px;width:993px;height:771px;display:flex;box-shadow:4px 6px 10px rgba(0,0,0,.35)}
.panel{position:relative;height:100%;overflow:hidden}

/* FAQ panel */
.panel--faq{width:323px;background:linear-gradient(160deg,#27507c 0%,var(--navy) 45%,#1a355a 100%);font-family:"Montserrat",sans-serif}
.faq-title{position:absolute;left:64px;top:44px;font-size:64px;font-weight:500;color:var(--sky);letter-spacing:-1px}
.faq-item{position:absolute;left:33px;width:258px}
.faq-item h3{font-size:14.5px;font-weight:500;color:var(--sky);margin-bottom:6px;letter-spacing:.2px}
.faq-item p{font-size:11.2px;line-height:13.3px;color:var(--white);text-align:justify}

/* Contact panel */
.panel--contact{width:328px;background:linear-gradient(180deg,var(--ink) 0%,#050b17 55%,#0b2a5c 100%);font-family:"Montserrat",sans-serif;text-align:center}
.brand-mini{position:absolute;top:52px;left:0;width:100%;font-size:20px;font-weight:600;color:var(--bright);line-height:22px;letter-spacing:.5px}
.contact{position:absolute;top:131px;left:0;width:100%;font-size:11.3px;line-height:13.6px;color:var(--white)}
.contact span{color:var(--bright)}
.figure-art{position:absolute;left:10px;top:230px;width:308px;height:541px;background:radial-gradient(ellipse 35% 55% at 50% 48%,rgba(90,170,255,.75) 0%,rgba(30,90,200,.35) 45%,rgba(5,15,40,0) 75%),radial-gradient(ellipse 60% 18% at 50% 100%,rgba(180,220,255,.55),rgba(0,0,0,0) 70%)}

/* Cover panel */
.panel--cover{width:342px;background:linear-gradient(180deg,#0f3a6a 0%,var(--navy-deep) 40%,#0a2c57 100%);font-family:"Oswald",sans-serif;color:var(--white);text-align:center}
.cover-wave{position:absolute;left:0;top:0;width:342px;height:771px}
.brand{position:absolute;top:104px;left:0;width:100%;font-family:"Montserrat",sans-serif;font-weight:600;font-size:25px;line-height:25px;color:var(--white);letter-spacing:.5px}
.brand small{display:block;font-size:12px;line-height:14px;letter-spacing:2px}
.headline{position:absolute;top:192px;left:0;width:100%;font-weight:700;font-size:50px;line-height:60px;letter-spacing:.5px}
.headline em{font-style:normal;color:var(--bright)}
.chamber-art{position:absolute;left:50px;top:302px;width:252px;height:400px;background:linear-gradient(90deg,#4d5962 0%,#7b8891 30%,#3a4650 55%,#1c2f8f 70%,#23388f 100%);border-radius:4px 60px 0 0;opacity:.9}
.rule{position:absolute;left:0;width:342px;height:4px;background:var(--bright)}
.offer{position:absolute;top:440px;left:0;width:100%;font-weight:500;font-size:33px;line-height:37px;text-shadow:0 2px 4px rgba(0,0,0,.5)}
.offer .big{font-size:60px;font-weight:700;color:var(--bright);vertical-align:-6px;line-height:37px}
.offer .accent{color:var(--bright)}
.cta{position:absolute;top:711px;left:0;width:100%;font-weight:500;font-size:19px}
.cta-url{position:absolute;top:739px;left:0;width:100%;font-family:"Montserrat",sans-serif;font-size:10.5px;letter-spacing:.5px}
.cta-url span{color:var(--bright)}
</style>
</head>
<body>
<div class="canvas">
  <div class="brochure">

    <section class="panel panel--faq">
      <h2 class="faq-title">FAQs</h2>
      <div class="faq-item" style="top:145px">
        <h3>LOREM IPSUM DOLOR SIT AMET</h3>
        <p>Lorem ipsum dolor sit amet, consectetur adipiscing elit, sed do eiusmod tempor incididunt ut labore et dolore magna aliqua. Ut enim ad minim veniam, quis nostrud exercitation ullamco laboris nisi ut aliquip ex ea commodo consequat. Duis aute irure dolor in reprehenderit in voluptate velit esse cillum dolore eu fugiat nulla pariatur. Excepteur sint occaecat cupidatat non proident, sunt in culpa qui officia deserunt mollit anim id est laborum</p>
      </div>
      <div class="faq-item" style="top:355px">
        <h3>LOREM IPSUM DOLOR SIT AMET</h3>
        <p>Lorem ipsum dolor sit amet, consectetur adipiscing elit, sed do eiusmod tempor incididunt ut labore et dolore magna aliqua. Ut enim ad minim veniam, quis nostrud exercitation ullamco laboris nisi ut aliquip ex ea commodo consequat. Duis aute irure dolor in reprehenderit in voluptate velit esse cillum dolore eu fugiat nulla pariatur. Excepteur sint occaecat cupidatat non proident, sunt in culpa qui officia deserunt mollit anim id est laborum</p>
      </div>
      <div class="faq-item" style="top:566px">
        <h3>LOREM IPSUM DOLOR SIT AMET</h3>
        <p>Lorem ipsum dolor sit amet, consectetur adipiscing elit, sed do eiusmod tempor incididunt ut labore et dolore magna aliqua. Ut enim ad minim veniam, quis nostrud exercitation ullamco laboris nisi ut aliquip ex ea commodo consequat. Duis aute irure dolor in reprehenderit in voluptate velit esse cillum dolore eu fugiat nulla pariatur. Excepteur sint occaecat cupidatat non proident, sunt in culpa qui officia deserunt mollit anim id est laborum</p>
      </div>
    </section>

    <section class="panel panel--contact">
      <div class="brand-mini">TIDEWELL<br>CRYOTHERAPY</div>
      <div class="contact">
        <span>Phone:</span> 001-2345-678<br>
        <span>Address:</span> your location<br>
        <span>Email:</span> youremail@domain.com<br>
        <span>Website:</span> www.yourwebsite.com
      </div>
      <div class="figure-art" role="img" aria-label="Glowing blue translucent human figure floating with arms outstretched, showing the skeleton"></div>
    </section>

    <section class="panel panel--cover">
      <svg class="cover-wave" viewBox="0 0 342 771" aria-hidden="true">
        <path d="M0 190 C80 175 150 205 230 170 C280 150 320 140 342 140 L342 771 L0 771 Z" fill="#0d3567" opacity=".8"/>
        <path d="M0 190 C80 175 150 205 230 170 C280 150 320 140 342 140" fill="none" stroke="#2a6fb8" stroke-width="2" opacity=".6"/>
      </svg>
      <div class="brand">TIDEWELL<small>CRYOTHERAPY</small></div>
      <div class="chamber-art" role="img" aria-label="Whole body cryotherapy chamber with open door and blue lights"></div>
      <h1 class="headline">WHOLE <em>BODY</em><br><em>CRYO</em>THERAPY</h1>
      <div class="rule" style="top:440px"></div>
      <div class="offer">JUST <span class="big">3</span> MINUTES<br>FOR WHOLE BODY<br><span class="accent">RECOVERY</span></div>
      <div class="rule" style="top:562px"></div>
      <div class="rule" style="top:702px"></div>
      <div class="cta">BOOK YOUR APPOINTMENT TODAY</div>
      <div class="cta-url">WWW.<span>YOURDOMAIN</span>.COM</div>
    </section>

  </div>
</div>
</body>
</html>
```